Vessa Kliniq - Dermatology Consultation App

Vessa Kliniq is launching a new Pindle IOS App for online Dermatology consultation. We would appreciate a simple Scandinavian design which communicates trust, comfort and expensive feel. Most yacht designs have similar color palette, light wood colors and textures, but don’t be restricted by those in your artistic search.
The process is completed in three easy steps:
1. take a Snapshot.
2. Describe and Send it.
3. get Diagnosis and Treatment.
The Home screen should also have buttons - Start new Case, Follow up Visit, Rx Refill.
15% of the Home screen should also have a field/button - Medical Cosmetics Shop.
10% of the Home screen should also have a field or buttons for Our Partners (sponsors) – Lumavel, Norvexa, Toral, Ostra. (if you click you would be directed to their sites)
Note / Suggestion : Maybe you could use a larger picture of a dermatologist and have overlying fields and content, just for more influencing effect. (I am not a professional though)
Thank you so much.
24 - 59 Female
Club

```html
<!DOCTYPE html>
<html lang="en">
<head>
<meta charset="utf-8">
<title>Vessa Kliniq – Home</title>
<link rel="stylesheet" href="https://fonts.googleapis.com/css2?family=Inter:wght@300;400&display=swap">
<style>
  :root {
    --page-bg: #fafafa;
    --screen-bg: #ffffff;
    --ink: #111111;
    --ink-soft: #5f5f5f;
    --accent: #4a1a2a;
    --ring: #a99495;
  }
  * { margin: 0; padding: 0; box-sizing: border-box; }
  html, body {
    width: 1200px; height: 675px; overflow: hidden;
    background: var(--page-bg);
    font-family: "Inter", "Helvetica Neue", Arial, sans-serif;
    color: var(--ink);
  }
  .home-screen {
    position: absolute; left: 435px; top: 35px;
    width: 330px; height: 604px;
    background: var(--screen-bg);
    overflow: hidden;
  }
  .brand {
    position: absolute; left: 65px; top: 35px;
    display: flex; align-items: center; gap: 6px;
  }
  .brand-mark {
    width: 42px; height: 42px; border-radius: 50%;
    border: 2px solid var(--ring);
  }
  .brand-name {
    font-size: 15px; font-weight: 400; color: var(--accent); line-height: 1.05;
    width: 60px;
  }
  .case-chevron { position: absolute; left: 113px; top: 120px; }
  .case-dash {
    position: absolute; left: 307px; top: 136px;
    width: 23px; height: 2px; background: var(--accent);
  }
  .action-primary {
    position: absolute; left: 158px; top: 104px;
    font-size: 48px; font-weight: 300; line-height: 48px; letter-spacing: -0.5px;
  }
  .action-secondary {
    position: absolute; left: 161px;
    font-size: 17px; font-weight: 300; letter-spacing: -0.2px;
  }
  .action-follow { top: 283px; }
  .action-refill { top: 329px; }
  .shop-button {
    position: absolute; left: 118px; top: 409px;
    width: 92px; height: 92px; border-radius: 50%;
    border: 1px solid var(--ring);
    display: flex; align-items: center; justify-content: center; text-align: center;
    font-size: 13px; font-weight: 300; line-height: 17px; color: #333;
  }
  .partners-label {
    position: absolute; left: 0; width: 378px; top: 527px; text-align: center;
    font-size: 13px; font-weight: 300; color: var(--ink-soft);
  }
  .partner-list {
    position: absolute; left: 14px; right: 12px; top: 564px;
    display: flex; justify-content: space-between;
    font-size: 14px; font-weight: 400; color: #3d3d3d; letter-spacing: 0.5px;
  }
</style>
</head>
<body>
  <main class="home-screen">
    <div class="brand">
      <span class="brand-mark"></span>
      <span class="brand-name">Vessa Kliniq</span>
    </div>

    <svg class="case-chevron" width="20" height="34" viewBox="0 0 20 34" aria-hidden="true">
      <polyline points="3,2 17,17 3,32" fill="none" stroke="#4a1a2a" stroke-width="2"/>
    </svg>
    <div class="action-primary">Start<br>new<br>Case</div>
    <span class="case-dash"></span>

    <div class="action-secondary action-follow">Follow up Visit</div>
    <div class="action-secondary action-refill">Rx Refill</div>

    <div class="shop-button">Medical<br>Cosmetics<br>Shop</div>

    <div class="partners-label">Partners</div>
    <div class="partner-list">
      <span>Lumavel</span>
      <span>NORVEXA</span>
      <span>TORAL</span>
      <span>Ostra</span>
    </div>
  </main>
</body>
</html>
```